Stylist/Barber Standup Sign for Hair Regrowth Company

We want to design an attractive and eye-catching sign for hair stylists and barbers to sit on their workstations to attract the attention of their clients regarding hair loss and encourage them to speak to their stylist about it of they are would like to seek treatment.
50% of men and 25% of women suffer from hair loss but most are in denial that it is happening or too embarrassed to talk about it.

Copy for the flyer is as follows:

[Section 1:]
This flyer has been placed here/designed to spark conversation about hair loss

[Section 2:]
The truth is...
73% of people believe their hair is thinning
They are right

[Section 3:]
If you've got questions, your stylist or barber has answers.

Additional Background Information:

Primary target audience is men between the ages of 25-45, secondary target audience is men 46-60

Current Consumer Perception? (in the first person) “I’ve been thinking about my hair. I think it’s getting thinner and I’m scared, worried and don’t know what to do. But I don’t know if there is anything that really works. I’ve tried other things and nothing‘s worked.”

Tonality of materials? Very guy friendly, matter of fact, authoritative, its what you might hear from your best friend. Confident. Encouraging, but with a sense of urgency.

Please use our brand colors, but do not include our logo or brand name.
Colors are as follows:
Green: #4ca26f
Light Grey: #999999
Dark Grey: #262626

I have attached print templates in both PDF and Jpeg, please use those to provide final ready to print documents if you are selected.

Target Market(s)

Industry/Entity Type

Health And Wellness

Font styles to use
Sans Serif

Colors
00a990
ffffff
333333
cbcbcb

Requirements
Must have
• We want to get across the following messaging. Ideally you will submit a design using our copy and if you think you can do better, please feel free to submit another design with your own copy/messaging. If you can do it better we would love to select you :-)
• Our copy?
• This flyer has been placed here/designed to spark conversation about hair loss
• The truth is...
• 73% of people believe their hair is thinning
• They are right
• If you've got questions, your stylist or barber has answers
• Also please use our brand colors:
• Green: #4ca26f
• Light Grey: #999999
• Dark Grey: #262626
Should not have
• dont add any logos, images or ornate design. this needs to be simple, easy to ready and eye catching.
• do not use the color red in any capacity.

```html
<!DOCTYPE html>
<html lang="en">
<head>
<meta charset="utf-8">
<title>Hair Loss Conversation Standup Sign</title>
<link rel="stylesheet" href="https://fonts.googleapis.com/css2?family=Oswald:wght@700&family=Lato:ital,wght@0,400;1,400;1,700&display=swap">
<style>
  :root {
    --teal: #00a990;
    --teal-soft: #7fcbb8;
    --teal-light: #9fd8c9;
    --ink: #1a1a1a;
    --charcoal: #333333;
    --black: #141414;
    --silver: #cbcbcb;
    --paper: #ffffff;
    --rule: #9a9a9a;
  }
  html, body {
    margin: 0;
    padding: 0;
    width: 900px;
    height: 1200px;
    overflow: hidden;
    background: var(--paper);
  }
  .canvas {
    position: relative;
    width: 900px;
    height: 1200px;
    background: var(--paper);
    font-family: "Lato", Arial, sans-serif;
    color: var(--ink);
  }
  .artwork {
    position: absolute;
    inset: 0;
  }
  .headline {
    position: absolute;
    left: 270px;
    width: 530px;
    text-align: center;
    font-family: "Oswald", "Arial Narrow", sans-serif;
    font-weight: 700;
    line-height: 1;
    margin: 0;
    text-transform: uppercase;
  }
  .headline-top {
    top: 262px;
    font-size: 84px;
    color: var(--ink);
    letter-spacing: 1px;
    left: 268px;
  }
  .headline-bottom {
    top: 338px;
    font-size: 82px;
    color: var(--paper);
    left: 262px;
  }
  .headline-reflection {
    top: 410px;
    font-size: 82px;
    color: var(--paper);
    left: 262px;
    transform: scaleY(-1);
    opacity: 0.45;
    height: 48px;
    overflow: hidden;
    -webkit-mask-image: linear-gradient(to top, rgba(0,0,0,0.9), rgba(0,0,0,0) 75%);
    mask-image: linear-gradient(to top, rgba(0,0,0,0.9), rgba(0,0,0,0) 75%);
  }
  .headline-reflection span {
    display: block;
    margin-top: -34px;
  }
  .intro {
    position: absolute;
    left: 140px;
    top: 620px;
    width: 640px;
    margin: 0;
    font-style: italic;
    font-size: 20.5px;
    line-height: 28px;
  }
  .truth-banner {
    position: absolute;
    left: 100px;
    top: 704px;
    width: 236px;
    height: 34px;
    background: var(--teal);
    clip-path: polygon(0 0, 100% 0, 88% 100%, 0 100%);
    color: var(--paper);
    font-weight: 700;
    font-style: italic;
    font-size: 20px;
    line-height: 34px;
    padding-left: 40px;
    box-sizing: border-box;
    margin: 0;
  }
  .truth-fact {
    position: absolute;
    left: 140px;
    top: 754px;
    margin: 0;
    font-style: italic;
    font-size: 21px;
    line-height: 30px;
  }
  .column {
    position: absolute;
    top: 814px;
    margin: 0;
    font-style: italic;
    font-size: 20.5px;
    line-height: 28px;
    text-align: justify;
  }
  .column-tone {
    left: 140px;
    width: 352px;
  }
  .column-divider {
    position: absolute;
    left: 515px;
    top: 826px;
    width: 1px;
    height: 140px;
    background: var(--rule);
  }
  .column-answers {
    left: 536px;
    width: 228px;
  }
  .website {
    position: absolute;
    left: 150px;
    top: 1082px;
    margin: 0;
    font-size: 11px;
    letter-spacing: 3px;
    color: var(--paper);
  }
  .call-line {
    position: absolute;
    left: 490px;
    top: 1062px;
    margin: 0;
    font-style: italic;
    font-size: 25px;
    color: var(--charcoal);
    white-space: nowrap;
  }
  .call-line .phone {
    font-size: 22px;
  }
</style>
</head>
<body>
<main class="canvas">
  <svg class="artwork" width="900" height="1200" viewBox="0 0 900 1200" aria-hidden="false">
    <defs>
      <linearGradient id="interior-tone" x1="0" y1="0" x2="0" y2="1">
        <stop offset="0" stop-color="#d9d9d9"/>
        <stop offset="0.35" stop-color="#eeeeee"/>
        <stop offset="0.6" stop-color="#f6f6f6"/>
        <stop offset="1" stop-color="#dcdcdc"/>
      </linearGradient>
      <linearGradient id="diamond-fill" x1="0" y1="0" x2="0" y2="1">
        <stop offset="0" stop-color="#7fcbb8"/>
        <stop offset="1" stop-color="#0fae93"/>
      </linearGradient>
      <linearGradient id="corner-fill" x1="0" y1="0" x2="0" y2="1">
        <stop offset="0" stop-color="#7fcbb8"/>
        <stop offset="1" stop-color="#1fb39a"/>
      </linearGradient>
    </defs>

    <!-- sign sheet -->
    <rect class="sheet" x="100" y="72" width="700" height="1038" fill="var(--paper)"/>
    <rect class="interior-backdrop" x="100" y="72" width="700" height="1038" fill="url(#interior-tone)" role="img" aria-label="Soft grey photo of a bright salon interior"/>
    <rect class="text-wash" x="100" y="600" width="700" height="380" fill="#ffffff" opacity="0.55"/>

    <!-- top-left corner -->
    <polygon class="corner-black" points="100,72 332,72 100,332" fill="var(--black)"/>
    <polygon class="corner-teal" points="332,72 380,72 100,362 100,332" fill="var(--teal)"/>
    <polygon class="corner-band" points="380,72 800,72 800,130 100,395 100,362" fill="#ffffff" opacity="0.35"/>

    <!-- stacked diamonds -->
    <polygon class="diamond-teal-back" points="372,275 537,440 372,605 207,440" fill="var(--teal)"/>
    <polygon class="diamond-frame" points="360,180 540,360 360,540 180,360" fill="var(--black)"/>
    <polygon class="diamond-frame-inner" points="360,198 522,360 360,522 198,360" fill="#ebebeb"/>

    <polygon class="diamond-halo" points="530,77 795,342 530,607 265,342" fill="var(--teal-soft)" opacity="0.85"/>
    <polygon class="diamond-border" points="530,95 777,342 530,589 283,342" fill="var(--paper)"/>
    <polygon class="diamond-main" points="530,110 762,342 530,574 298,342" fill="url(#diamond-fill)"/>

    <!-- bottom corners -->
    <polygon class="footer-teal-strip" points="100,975 445,1104 430,1110 100,992" fill="var(--teal)"/>
    <polygon class="footer-black" points="100,992 430,1110 100,1110" fill="var(--black)"/>
    <polygon class="footer-teal" points="410,1110 800,958 800,1110" fill="url(#corner-fill)"/>
  </svg>

  <h1 class="headline headline-top">Lorem</h1>
  <p class="headline headline-bottom">Ipsum</p>
  <p class="headline headline-reflection" aria-hidden="true"><span>Ipsum</span></p>

  <p class="intro">50% of men and 25% of women suffer from hair loss but most are in denial that it is happening or too embarrassed to talk about it.</p>

  <h2 class="truth-banner">THE TRUTH IS...</h2>
  <p class="truth-fact">73% of people believe their hair is thinning ....they are right</p>

  <p class="column column-tone">Tonality of materials? Very guy friendly, matter of fact, authoritative, its what you might hear from your best friend. Confident.&nbsp; Encouraging , but with a sense of urgency.</p>
  <div class="column-divider"></div>
  <p class="column column-answers">If you've got questions, your stylist or barber has answers.</p>

  <p class="website">www.yourwesite.com</p>
  <p class="call-line">call us today-<span class="phone">123 1234 123</span></p>
</main>
</body>
</html>
```